Branvique needs a business Card Design

We are looking for a business card Design for our new Managed Service Provider Company, Branvique. Branvique encompasses everything IT for the average medium sized business. Our primary services are help desk support, cyber-security (malware and ransomware protection), and Disaster Recovery systems. We would like the design to have a very clean and professional look, with a very minimalist feel.

Target Market(s)

Medium to large sized businesses

Industry/Entity Type

It Service

Contact Information for Business Card

Name GoesHere
name@branvique.com
O: 555-382-6047
C: 555-731-5820

Font styles to use
Other font styles liked:
• Poppins Font Only Please

Colors

Designer to choose only greyscale colors for use in the design.

Requirements
Must have
• Logo included
Nice to have
• Cutting Edge, innovative, minimalistic, elegant

```html
<!DOCTYPE html>
<html lang="en">
<head>
<meta charset="utf-8">
<title>Branvique Business Card</title>
<link href="https://fonts.googleapis.com/css2?family=Poppins:wght@300;400;500;600&display=swap" rel="stylesheet">
<style>
  :root {
    --navy: #13273d;
    --paper: #f4f4f4;
    --page: #ffffff;
    --ink: #13273d;
    --white: #ffffff;
    --pattern: #22364f;
  }
  * { margin: 0; padding: 0; box-sizing: border-box; }
  html, body {
    width: 1200px; height: 1200px; overflow: hidden;
    background: var(--page);
    font-family: "Poppins", sans-serif;
    color: var(--ink);
  }
  .canvas { position: relative; width: 1200px; height: 1200px; }

  .card {
    position: absolute; top: 294px;
    width: 395px; height: 611px;
    background: var(--paper);
    overflow: hidden;
  }
  .card--front { left: 193px; }
  .card--back { left: 612px; }

  .edge-band {
    position: absolute; top: 0; bottom: 0; width: 22px;
    background: var(--navy);
  }
  .edge-band--left { left: 0; }
  .edge-band--right { right: 0; }

  .center-text {
    position: absolute; left: 0; right: 0;
    text-align: center; white-space: nowrap;
  }

  .brand-square {
    position: absolute; left: 50%;
    width: 36px; height: 36px; margin-left: -18px;
    background: currentColor;
  }
  .card--front .brand-square { top: 52px; color: var(--navy); }

  .wordmark {
    font-weight: 500; font-size: 27px;
    letter-spacing: 0.5em; text-indent: 0.5em;
    line-height: 1;
  }
  .card--front .wordmark { top: 139px; }

  .holder-name { top: 262px; font-size: 23px; font-weight: 300; }
  .holder-name strong { font-weight: 500; }
  .holder-email { top: 306px; font-size: 23px; font-weight: 500; }
  .holder-phone { font-size: 23px; font-weight: 300; }
  .holder-phone b { font-weight: 500; }
  .holder-phone--office { top: 350px; }
  .holder-phone--cell { top: 395px; }

  .website {
    font-size: 18px; font-weight: 400;
    letter-spacing: 0.22em; text-indent: 0.22em;
  }
  .card--front .website { top: 554px; }

  .back-panel {
    position: absolute; top: 0; bottom: 0; left: 22px; right: 22px;
    background: linear-gradient(160deg, var(--navy) 0%, var(--pattern) 50%, var(--navy) 100%);
    color: var(--white);
  }
  .back-panel .brand-square { top: 246px; color: var(--white); }
  .back-panel .wordmark { top: 334px; }
  .back-panel .website { top: 364px; font-weight: 300; font-size: 17px; letter-spacing: 0.16em; text-indent: 0.16em; }
</style>
</head>
<body>
<main class="canvas">
  <section class="card card--front" aria-label="Business card front">
    <div class="edge-band edge-band--left"></div>
    <div class="edge-band edge-band--right"></div>
    <div class="brand-square"></div>
    <p class="center-text wordmark">BRANVIQUE</p>
    <p class="center-text holder-name">Name <strong>Last Name</strong></p>
    <p class="center-text holder-email">name@branvique.com</p>
    <p class="center-text holder-phone holder-phone--office"><b>O:</b> 555-382-6047</p>
    <p class="center-text holder-phone holder-phone--cell"><b>C:</b> 555-731-5820</p>
    <p class="center-text website">www.branvique.com</p>
  </section>

  <section class="card card--back" aria-label="Business card back">
    <div class="back-panel" role="img" aria-label="Navy panel with a subtle repeating pattern of thin vertical strokes">
      <div class="brand-square"></div>
      <p class="center-text wordmark">BRANVIQUE</p>
      <p class="center-text website">www.branvique.com</p>
    </div>
  </section>
</main>
</body>
</html>
```